Letterhead design for Sleep Consulting Business

I'm looking for a new letterhead (heading/footer) design for my Sleep Consulting Business, I work with families to help their children improve their sleep.

The heading/footer will used in Microsoft Word Only-to be used for all of my documents such as writing Sleep Plans. I need to utilize as much working space in the document as possible. This will NOT be printed out on paper- it will only be used for heading/footer on microsoft word, then emailed to clients, who may print it at home.

My brand colors:
Dark Blue Hex: 1F2A42
Lighter Blueish Hex: 90BEC9
You're welcome to check out my website for inspiration- it is freshly created with other colors as well, and I love the outcome. www.hollowpinerest.com

Target Market(s)

Tired parents

Font styles to use
Script
Other font styles liked:
• Great Vibe, Lato or Just Another Hand are all used currently for my brand. Open to other options.

Requirements
Must have
• The letterhead (heading/footer) MUST be kept narrow (height-wise), so I have plenty of space on my document, while including important information.

It should look professional on screen, and when printed.

Must include my business name OR logo (Hollow Pine Sleep Consulting), and my email address. Mara@hollowpinerest.com

Website is optional, not required, just if you need to fill in a spot: www.hollowpinerest.com

```html
<!DOCTYPE html>
<html lang="en">
<head>
<meta charset="utf-8">
<title>Hollow Pine Sleep Consulting – Letterhead</title>
<link href="https://fonts.googleapis.com/css2?family=Nunito:wght@600;700&family=Quicksand:wght@400&display=swap" rel="stylesheet">
<style>
  :root {
    --navy: #1F2A42;
    --sky: #90BEC9;
    --grey: #C9C9C9;
    --backdrop: #E6E6E6;
    --paper: #FFFFFF;
    --ink: #222222;
  }
  * { margin: 0; padding: 0; box-sizing: border-box; }
  html, body { width: 1000px; height: 1200px; overflow: hidden; background: var(--backdrop); }
  .canvas { position: relative; width: 1000px; height: 1200px; }
  .sheet { position: absolute; left: 95px; top: 30px; width: 810px; height: 1140px; background: var(--paper); overflow: hidden; }

  .brand { position: absolute; left: 120px; top: 108px; display: flex; align-items: center; gap: 20px; height: 76px; }
  .brand-mark { width: 76px; height: 76px; border-radius: 50%; background: var(--navy); flex: none; }
  .brand-name { font-family: "Nunito", sans-serif; font-weight: 600; font-size: 30px; line-height: 36px; color: var(--navy); white-space: nowrap; }

  .recipient { position: absolute; left: 120px; top: 233px; font-family: "Nunito", sans-serif; font-weight: 700; font-style: normal; font-size: 16px; line-height: 20.3px; color: var(--sky); }

  .letter-body { position: absolute; left: 120px; top: 380px; width: 570px; font-family: "Quicksand", sans-serif; font-size: 18px; letter-spacing: 0.15px; line-height: 22.8px; color: var(--navy); text-align: justify; hyphens: auto; -webkit-hyphens: auto; }
  .letter-body p + p { margin-top: 22.8px; }

  .signature { position: absolute; left: 126px; top: 762px; font-family: "Nunito", sans-serif; font-weight: 700; color: var(--sky); }
  .signature-name { font-size: 40px; line-height: 50px; }
  .signature-title { font-size: 20px; line-height: 26px; }

  .contacts { position: absolute; left: 126px; top: 890px; list-style: none; }
  .contact { display: flex; align-items: flex-start; gap: 17px; height: 49px; }
  .contact-icon { width: 31px; height: 31px; display: flex; align-items: center; justify-content: center; background: var(--navy); flex: none; }
  .contact-icon.is-light { background: var(--sky); }
  .contact-text { font-family: "Nunito", sans-serif; font-weight: 700; font-size: 12.5px; line-height: 19px; color: var(--ink); margin-top: -2px; }

  .footer-bands { position: absolute; left: 0; bottom: 0; width: 810px; height: 72px; }
</style>
</head>
<body>
<div class="canvas">
  <div class="sheet">
    <header class="brand">
      <div class="brand-mark"></div>
      <div class="brand-name">Hollow Pine Sleep Consulting</div>
    </header>

    <address class="recipient">
      TO<br>
      Dana Whitfield<br>
      Human Resources<br>
      Brightfield Inc.<br>
      2207-B Alder Row, Fenwick<br>
      E42 USA
    </address>

    <main class="letter-body">
      <p>A Lorem ipsum dolor sit amet, consectetuer adipiscing elit, sed diam nonmmy nibh euismod tincidunt ut laoreet dolore magna aliquam erat volutpat. Ut wisi enim ad minim veniam, quis nostrud exerci tationmcorper suscipit lobortis nisl ut aliquip ex ea commodo consequat. Duis autem vel eum iriure dolor in hendrerit in vulputate velit esse molestie consequat, vel illum dolore eu feugiat nulla facilisis at vero eros et accumsan et iusto odio dignissim qui blandit praesent luptatum zzril delenit augue duis dolore te feugait nulla facilisi.</p>
      <p>Nam liber tempor cum soluta nobis eleifend option congue nihil imprdiet doming id quod mazim placerat facer possim assum. Typi non habent claritatem insitam;</p>
      <p>Est usus legentis in iis qui facit eorum claritatem.</p>
    </main>

    <section class="signature">
      <div class="signature-name">Owen Hartley</div>
      <div class="signature-title">Managing Director</div>
    </section>

    <ul class="contacts">
      <li class="contact">
        <span class="contact-icon">
          <svg width="15" height="15" viewBox="0 0 24 24" aria-hidden="true"><path fill="#fff" d="M6.6 10.8a15.2 15.2 0 0 0 6.6 6.6l2.2-2.2c.3-.3.7-.4 1-.2 1.1.4 2.3.6 3.6.6.6 0 1 .4 1 1V20c0 .6-.4 1-1 1A17 17 0 0 1 3 4c0-.6.4-1 1-1h3.5c.6 0 1 .4 1 1 0 1.3.2 2.5.6 3.6.1.3 0 .7-.2 1z"/></svg>
        </span>
        <span class="contact-text">+000 12345 6789<br>+000 12345 6789</span>
      </li>
      <li class="contact">
        <span class="contact-icon is-light">
          <svg width="15" height="15" viewBox="0 0 24 24" aria-hidden="true" fill="none" stroke="#fff" stroke-width="1.8"><circle cx="12" cy="12" r="9"/><ellipse cx="12" cy="12" rx="4" ry="9"/><path d="M3 12h18M5 7h14M5 17h14"/></svg>
        </span>
        <span class="contact-text">Mara@hollowpinerest.com<br>www.hollowpinerest.com</span>
      </li>
      <li class="contact">
        <span class="contact-icon">
          <svg width="14" height="16" viewBox="0 0 24 24" aria-hidden="true"><path fill="#fff" d="M12 2a7 7 0 0 0-7 7c0 5.2 7 13 7 13s7-7.8 7-13a7 7 0 0 0-7-7zm0 9.5A2.5 2.5 0 1 1 12 6.5a2.5 2.5 0 0 1 0 5z"/></svg>
        </span>
        <span class="contact-text">Street Address Here<br>Singapore, 2222</span>
      </li>
    </ul>

    <svg class="footer-bands" viewBox="0 0 810 72" aria-hidden="true">
      <rect x="0" y="20" width="495" height="22" fill="var(--grey)"/>
      <rect x="0" y="42" width="810" height="30" fill="var(--sky)"/>
      <polygon points="500,0 810,0 810,42 467,42" fill="var(--navy)"/>
      <polygon points="510,57 810,57 810,72 500,72" fill="var(--navy)"/>
    </svg>
  </div>
</div>
</body>
</html>
```